New Modern floristry business design

Hi, we are a new business based in Sydney called "copper fern floristry"

With so many floristry's we need a good design that will set a great first impression.

A few descriptive words on how we envision copper fern floristry:

-dynamic design
-minimal colour (colour can be used to enhance the design)
-black white grey (can include gold,silver,metallic shadowing)
Strong "COPPER FERN" with a classy "FLORISTRY"
Bold with a touch of feminine

Copper Fern Floristry,
Delia Varnet,
Copperfernfloristry@mailbay.com.au

```html
<!DOCTYPE html>
<html lang="en">
<head>
<meta charset="utf-8">
<title>Copper Fern Floristry – Business Cards</title>
<link rel="stylesheet" href="https://fonts.googleapis.com/css2?family=Pinyon+Script&display=swap">
<style>
  :root {
    --backdrop: #4b4b4e;
    --card: #050505;
    --gold: #d9b85c;
    --gold-soft: #b89a52;
    --foliage: rgba(120, 110, 82, 0.55);
    --foliage-fade: rgba(120, 110, 82, 0);
  }
  * { box-sizing: border-box; margin: 0; padding: 0; }
  html, body {
    width: 1200px;
    height: 800px;
    overflow: hidden;
    background: var(--backdrop);
  }
  .canvas {
    position: relative;
    width: 1200px;
    height: 800px;
    display: flex;
    justify-content: center;
    align-items: center;
    gap: 90px;
  }
  .card {
    position: relative;
    width: 320px;
    height: 580px;
    background: var(--card);
    overflow: hidden;
    box-shadow: 0 10px 30px rgba(0, 0, 0, 0.45);
  }
  .foliage {
    position: absolute;
  }
  .foliage--top-left {
    top: -40px; left: -60px;
    width: 330px; height: 300px;
    background: radial-gradient(ellipse at 35% 35%, var(--foliage) 0%, rgba(120,110,82,0.3) 45%, var(--foliage-fade) 72%);
  }
  .foliage--top-band {
    top: -40px; left: -40px;
    width: 420px; height: 280px;
    background: radial-gradient(ellipse at 40% 30%, var(--foliage) 0%, rgba(120,110,82,0.3) 45%, var(--foliage-fade) 72%);
  }
  .foliage--bottom-right {
    bottom: -40px; right: -70px;
    width: 360px; height: 330px;
    background: radial-gradient(ellipse at 60% 60%, var(--foliage) 0%, rgba(120,110,82,0.3) 45%, var(--foliage-fade) 72%);
  }
  .foliage--bottom-wide {
    bottom: -30px; right: -60px;
    width: 390px; height: 360px;
    background: radial-gradient(ellipse at 55% 60%, var(--foliage) 0%, rgba(120,110,82,0.3) 45%, var(--foliage-fade) 72%);
  }
  .brand {
    position: absolute;
    left: 0; right: 0;
    text-align: center;
    font-family: "Pinyon Script", cursive;
    color: var(--gold);
    font-weight: 400;
    line-height: 1;
  }
  .brand__name { display: block; }
  .brand__tag { display: block; }
  .card--back .brand { top: 150px; }
  .card--back .brand__name { font-size: 44px; }
  .card--back .brand__tag { font-size: 32px; margin-top: 2px; padding-left: 60px; }
  .card--front .brand { top: 210px; }
  .card--front .brand__name { font-size: 58px; }
  .card--front .brand__tag { font-size: 42px; margin-top: 2px; padding-left: 70px; }
  .contact {
    position: absolute;
    left: 26px;
    top: 370px;
    font-family: "Pinyon Script", cursive;
    color: var(--gold);
  }
  .contact__name { font-size: 30px; line-height: 1.2; }
  .contact__email { font-size: 17px; color: var(--gold-soft); margin-top: 2px; }
</style>
</head>
<body>
  <main class="canvas">
    <section class="card card--back">
      <div class="foliage foliage--top-band" role="img" aria-label="Muted olive watercolour foliage and leaves"></div>
      <div class="foliage foliage--bottom-wide" role="img" aria-label="Muted olive watercolour foliage and flower buds"></div>
      <h1 class="brand">
        <span class="brand__name">Copper Fern</span>
        <span class="brand__tag">Floristry</span>
      </h1>
      <div class="contact">
        <p class="contact__name">Delia Varnet</p>
        <p class="contact__email">Email: Copperfernfloristry@mailbay.com.au</p>
      </div>
    </section>

    <section class="card card--front">
      <div class="foliage foliage--top-left" role="img" aria-label="Muted olive watercolour foliage and flower buds"></div>
      <div class="foliage foliage--bottom-right" role="img" aria-label="Muted olive watercolour foliage and leaves"></div>
      <h2 class="brand">
        <span class="brand__name">Copper Fern</span>
        <span class="brand__tag">Floristry</span>
      </h2>
    </section>
  </main>
</body>
</html>
```